Velo 3D Imaging
Simple
Corvane Dental Imaging, LLC
218 North Marlow Avenue Suite 4C Cherry Hill, NJ 08034
info@Velo3D-example.com
www.Velo3D-example.com
Do not need individual names of people on the card. These are to be given to other doctors who would refer to the business to have CT scans done for their patient

```html
<!DOCTYPE html>
<html lang="en">
<head>
<meta charset="utf-8">
<title>Corvane Dental Imaging – Stationery Set</title>
<link rel="stylesheet" href="https://fonts.googleapis.com/css2?family=Open+Sans:wght@400;600&display=swap">
<style>
  :root {
    --backdrop: #bfc0c2;
    --paper: #ffffff;
    --brand-blue: #2b7cc4;
    --brand-navy: #33466b;
    --text-grey: #5b6270;
    --body-grey: #6d727a;
    --window-grey: #d9dde3;
    --flap-top: #9fb0c6;
    --flap-bottom: #e6ebf1;
    --accent-circle: #8ec3ea;
  }
  * { box-sizing: border-box; margin: 0; padding: 0; }
  html, body { width: 1200px; height: 828px; overflow: hidden; }
  body {
    background: var(--backdrop);
    font-family: "Open Sans", Arial, sans-serif;
    position: relative;
  }

  /* Name lockup: one plain circle and the name in one weight and colour */
  .brand { display: flex; align-items: center; gap: 8px; color: var(--brand-navy); font-weight: 600; white-space: nowrap; }
  .brand-dot { border-radius: 50%; background: var(--accent-circle); flex: none; }

  /* Business card */
  .business-card {
    position: absolute; left: 199px; top: 204px; width: 324px; height: 175px;
    background: var(--paper); box-shadow: 0 1px 3px rgba(0,0,0,.15);
  }
  .business-card .brand { position: absolute; left: 16px; top: 24px; font-size: 14px; }
  .business-card .brand-dot { width: 24px; height: 24px; }
  .card-contact {
    position: absolute; left: 18px; top: 106px; font-size: 7px; line-height: 11px; color: var(--text-grey);
  }
  .card-band { position: absolute; left: 0; right: 0; bottom: 0; height: 18px; background: var(--brand-blue); }

  /* Envelope */
  .envelope { position: absolute; left: 43px; top: 396px; width: 533px; height: 408px; }
  .envelope-flap { position: absolute; left: 0; top: 0; width: 533px; height: 64px; }
  .envelope-body {
    position: absolute; left: 0; top: 60px; width: 533px; height: 348px; background: var(--paper);
    box-shadow: 0 1px 3px rgba(0,0,0,.15);
  }
  .envelope .brand { position: absolute; left: 18px; top: 36px; font-size: 16px; }
  .envelope .brand-dot { width: 30px; height: 30px; }
  .envelope-window {
    position: absolute; left: 18px; top: 161px; width: 132px; height: 96px;
    background: var(--window-grey); border-radius: 4px;
  }
  .envelope-address { position: absolute; left: 18px; top: 267px; font-size: 6.5px; color: var(--text-grey); }
  .envelope-band { position: absolute; left: 0; right: 0; top: 288px; height: 14px; background: var(--brand-blue); }
  .envelope-web { position: absolute; left: 0; right: 0; top: 314px; text-align: center; font-size: 7.5px; color: var(--brand-blue); }

  /* Letterhead */
  .letterhead {
    position: absolute; left: 605px; top: 72px; width: 588px; height: 744px;
    background: var(--paper); box-shadow: 0 1px 3px rgba(0,0,0,.15);
  }
  .letterhead .brand { position: absolute; left: 0; right: 0; top: 34px; justify-content: center; font-size: 19px; }
  .letterhead .brand-dot { width: 34px; height: 34px; }
  .letter-body { position: absolute; left: 54px; right: 54px; top: 306px; color: var(--body-grey); }
  .salutation { font-size: 8.5px; font-weight: 600; color: var(--brand-navy); margin-bottom: 12px; }
  .letter-body p { font-size: 6.6px; line-height: 10.6px; text-align: justify; margin-bottom: 10px; }
  .letter-footer { position: absolute; left: 0; right: 0; bottom: 0; }
  .letter-address { text-align: center; font-size: 6.5px; color: var(--text-grey); margin-bottom: 8px; }
  .letter-web { text-align: center; font-size: 7.5px; color: var(--brand-blue); margin-bottom: 8px; }
  .letter-band { height: 14px; background: var(--brand-blue); }
</style>
</head>
<body>

  <section class="business-card">
    <div class="brand">
      <div class="brand-dot"></div>
      <span class="brand-name">Corvane Dental Imaging, LLC</span>
    </div>
    <div class="card-contact">
      218 North Marlow Avenue Suite 4C Brookvale, NJ 08099<br>
      P 555-014-2207 &nbsp; F 555-014-2208 &nbsp; E info@corvane-example.com
    </div>
    <div class="card-band"></div>
  </section>

  <section class="envelope">
    <svg class="envelope-flap" viewBox="0 0 533 64" preserveAspectRatio="none" aria-hidden="true">
      <defs>
        <linearGradient id="flapShade" x1="0" y1="0" x2="0" y2="1">
          <stop offset="0" stop-color="#9fb0c6"/>
          <stop offset="1" stop-color="#e6ebf1"/>
        </linearGradient>
      </defs>
      <path d="M0 64 L0 58 Q266 -54 533 58 L533 64 Z" fill="url(#flapShade)"/>
    </svg>
    <div class="envelope-body">
      <div class="brand">
        <div class="brand-dot"></div>
        <span class="brand-name">Corvane Dental Imaging, LLC</span>
      </div>
      <div class="envelope-window"></div>
      <div class="envelope-address">218 North Marlow Avenue Suite 4C Brookvale, NJ 08099 &nbsp; P 555-014-2207 &nbsp; F 555-014-2208 &nbsp; E info@corvane-example.com</div>
      <div class="envelope-band"></div>
      <div class="envelope-web">www.corvane-example.com</div>
    </div>
  </section>

  <section class="letterhead">
    <div class="brand">
      <div class="brand-dot"></div>
      <span class="brand-name">Corvane Dental Imaging, LLC</span>
    </div>
    <div class="letter-body">
      <div class="salutation">Dear Sir / Madame</div>
      <p>Lorem ipsum dolor sit amet, consectetur adipiscing elit. Donec id orci ut lacus varius tempus vel sed nulla. Vestibulum ante ipsum primis in faucibus orci luctus et ultrices posuere cubilia curae. Suspendisse potenti. Aenean vel mauris sed lectus volutpat dictum. Integer convallis, nunc at porta cursus, arcu purus malesuada nibh, a dignissim nisl metus sed ligula. Fusce eget tortor quis augue tincidunt porta. Phasellus sit amet nibh a magna fermentum posuere. Curabitur aliquet risus vitae elit gravida, non sodales mi rhoncus. Sed at erat sit amet purus mollis faucibus vel non massa.</p>
      <p>In dignissim tincidunt tempor. Aenean metus metus, adipiscing ac aliquam vitae, pulvinar at leo. Duis porta facilisis risus, quis ullamcorper tellus mattis nec. Aliquam erat volutpat. In sodales congue nisi id blandit. Nunc eros sem, dapibus sed blandit nec, semper congue augue. Nunc magna risus, consequat vitae laoreet non, aliquam vel nisl. In volutpat dapibus odio, id iaculis mi accumsan quis. Curabitur euismod pellentesque turpis vitae dictum. Cras tincidunt tortor a purus porta, et tincidunt nulla consectetur. Mauris blandit lorem vel tellus feugiat, eget varius lacus commodo.</p>
      <p>Curabitur vehicula nunc eu odio bibendum hendrerit. Proin mollis risus sed risus tempor pretium. Maecenas posuere rutrum risus pretium in aliquam libero tristique. Maecenas hendrerit purus nec elit euismod dictum. Nam nec justo eu odio sollicitudin egestas at non diam. Mauris tempor tincidunt metus. Nunc malesuada tincidunt odio, a congue lectus ornare sit amet. Morbi tempus ante a sapien eleifend porta, metus fermentum erat, non pharetra mi dui vehicula arcu. Pellentesque vel mi mauris. Nullam eu consectetur enim. Phasellus et neque sed erat molestie lorem ziwult.</p>
      <p>Fusce vitae lorem lectus, ac molestie elit. Nunc sollicitudin ligula quis lorem faucibus. Praesent id arcu lorem condimentum venenatis. Etiam maximus volutpat turpis, sed a vulputate risus volutpat vel. Nullam mattis ante ut lacus auctor iaculis. Curabitur malesuada porttitor est, vitae congue risus tincidunt quis. Integer lorem nisl, pharetra vel lobortis et, euismod a mi. Phasellus porttitor purus diam sed ullamcorper. Maecenas mollis odio, congue vehicula elementum vitae, ornare vel diam. Nulla nec porttitor tortor. Vestibulum ac felis et neque sollicitudin dignissim.</p>
    </div>
    <div class="letter-footer">
      <div class="letter-address">218 North Marlow Avenue Suite 4C Brookvale, NJ 08099 &nbsp; P 555-014-2207 &nbsp; F 555-014-2208 &nbsp; E info@corvane-example.com</div>
      <div class="letter-web">www.corvane-example.com</div>
      <div class="letter-band"></div>
    </div>
  </section>

</body>
</html>
```